Meadowlark Learning Support Partners (MLSP)

This is a professional business card. Logo and picture are a must on the front of the card. I am an educational consultant. I have been consulting for the past three years for a company. I am now opening my own company. My goal for my consulting company is to eventually consult all over America.

Target Market(s)

Educators, schools, professionals

Industry/Entity Type

Consulting

Contact Information for Business Card

Picture/logo on front, simple modern design

Font styles to use
Serif

Colors
85abd2
0355a3
3176b5
cedeed

Requirements
Must have
• picture, logo,
• Dorotea Halvorsen, Ed.S
• address 5327 Quarry ridge Ln. Nashville, TN 37058
• Cell:616-555-0182
• Office: 629-555-0147
• www.Mlspwx.com
• halvorsendorotea@mailvexo.com

```html
<!DOCTYPE html>
<html lang="en">
<head>
<meta charset="utf-8">
<title>MLSP Business Card – Front and Back</title>
<link rel="stylesheet" href="https://fonts.googleapis.com/css2?family=Lexend:wght@400;600&family=Arimo:wght@700&display=swap">
<style>
  :root {
    --royal: #0355a3;
    --royal-deep: #0b3a80;
    --mid-blue: #3176b5;
    --sky: #85abd2;
    --mist: #cedeed;
    --paper: #ffffff;
    --stage: #eef1f5;
  }
  * { box-sizing: border-box; margin: 0; padding: 0; }
  html, body {
    width: 1200px;
    height: 499px;
    overflow: hidden;
    background: var(--stage);
  }
  .sheet {
    position: relative;
    width: 1200px;
    height: 499px;
  }
  .card {
    position: absolute;
    top: 96px;
    width: 560px;
    height: 306px;
    overflow: hidden;
    box-shadow: 0 2px 10px rgba(3, 40, 90, 0.12);
  }
  .card--front { left: 30px; background: var(--royal); color: var(--paper); }
  .card--back { left: 610px; background: var(--paper); color: var(--royal-deep); }

  .brand-dot {
    position: absolute;
    border-radius: 50%;
  }
  .brand-name {
    position: absolute;
    font-family: "Lexend", sans-serif;
    font-weight: 600;
    letter-spacing: 2px;
  }
  .brand-divider {
    position: absolute;
    width: 1.5px;
  }
  .brand-tagline {
    position: absolute;
    font-family: "Lexend", sans-serif;
    font-weight: 400;
  }

  /* Front */
  .card--front .brand-dot { left: 26px; top: 120px; width: 62px; height: 62px; background: var(--paper); }
  .card--front .brand-name { left: 100px; top: 134px; font-size: 27px; color: var(--paper); }
  .card--front .brand-divider { left: 206px; top: 110px; height: 80px; background: var(--mist); }
  .card--front .brand-tagline { left: 219px; top: 108px; font-size: 16px; line-height: 21.5px; color: var(--paper); }
  .holder-name {
    position: absolute;
    left: 17px;
    top: 283px;
    font-family: "Arimo", sans-serif;
    font-weight: 700;
    font-size: 15px;
    color: var(--paper);
  }
  .portrait {
    position: absolute;
    left: 318px;
    top: 0;
    width: 242px;
    height: 306px;
    background: linear-gradient(180deg, var(--mid-blue) 0%, var(--sky) 45%, var(--royal-deep) 100%);
  }

  /* Back */
  .card--back .brand-dot { left: 64px; top: 36px; width: 80px; height: 80px; background: var(--royal-deep); }
  .card--back .brand-name { left: 156px; top: 56px; font-size: 34px; color: var(--royal-deep); }
  .card--back .brand-divider { left: 312px; top: 24px; height: 102px; background: var(--royal-deep); }
  .card--back .brand-tagline { left: 328px; top: 24px; font-size: 21px; line-height: 25.5px; color: var(--royal-deep); }
  .contact {
    position: absolute;
    left: 0;
    top: 166px;
    width: 100%;
    text-align: center;
    font-family: "Arimo", sans-serif;
    font-weight: 700;
    font-size: 15.5px;
    line-height: 21.5px;
    color: var(--royal-deep);
    list-style: none;
  }
  .contact__email { font-size: 17.5px; line-height: 24px; }
</style>
</head>
<body>
<main class="sheet">
  <section class="card card--front" aria-label="Card front">
    <span class="brand-dot"></span>
    <span class="brand-name">MLSP</span>
    <span class="brand-divider"></span>
    <p class="brand-tagline">Meadowlark<br>Learning<br>Support<br>Partners</p>
    <p class="holder-name">Dorotea Halvorsen, Ed.S</p>
    <div class="portrait" role="img" aria-label="Portrait photo of Dorotea Halvorsen in a dark blazer and white blouse"></div>
  </section>

  <section class="card card--back" aria-label="Card back">
    <span class="brand-dot"></span>
    <span class="brand-name">MLSP</span>
    <span class="brand-divider"></span>
    <p class="brand-tagline">Meadowlark<br>Learning<br>Support<br>Partners</p>
    <ul class="contact">
      <li>Dorotea Halvorsen, Ed.S</li>
      <li>5327 Quarry ridge Ln. Nashville, TN 37058</li>
      <li>Cell:616-555-0182</li>
      <li>Office: 629-555-0147</li>
      <li>www.Mlspwx.com</li>
      <li class="contact__email">halvorsendorotea@mailvexo.com</li>
    </ul>
  </section>
</main>
</body>
</html>
```